Water Filter Company Needs Bizz Cards!!

Need business cards for my company. We sell whole home water filters and salt free water softeners. No more buying bottled water. Our filtering units filter out all heavy metals, chlorine, and VOC's, last 15 years, and are maintenance free and supply your whole home with spring quality alkaline water. Our Salt free water conditioners, eliminate hard water and scale, without lowering the ph, or TDS's (total Dissolved solids)

I think this is the color code we are using on my site. My logo looks good behind it. #192841

Website will be www.Brovexa.com

Industry/Entity Type

Water Purification

Contact Information for Business Card

For now, just insert standard Dummy text. I need these text lines for the info to be editable so i can make them for multiple employees. I do have Photoshop and illustrator, unless there is a simpler program i can use solely for biz cards

Font styles to use
Sans Serif

Requirements
Must have
• Use my preexisting logo.

www.BroVexa.com

Spring Quality Alkaline Water at every tap.

List out services. Whole Home Water Filters, Salt Free Water Softeners, Clarimont KT7, UV Sterilizers
Nice to have
• I think this is the color code we are using on my site. My logo looks good behind it. #192841 or black. Please no white or light blue backgrounds.

Maybe a picture of my tank.

Slogan like Spring Quality Alkaline Water at every tap.
And just list the services Whole Home Water Filters, Salt Free Water Softeners, Clarimont KT7, UV Sterilizers

I think I would like to not have a contrasting textured logo like I see on some of them. I may use it for my personal cards, but new employees may not want the extra expense.
Should not have
• A different logo than the one provided.

White or baby blue backgrounds. Use the color code, or blacks.

```html
<!DOCTYPE html>
<html lang="en">
<head>
<meta charset="utf-8">
<title>BroVexa Business Card</title>
<link href="https://fonts.googleapis.com/css2?family=Lato:wght@700&family=Roboto:wght@400;500;700&display=swap" rel="stylesheet">
<style>
  :root {
    --stage: #b9b9b9;
    --card-dark: #111111;
    --navy: #192841;
    --navy-lift: #223658;
    --blue-mid: #2dbdec;
    --blue-pale: #acd6ee;
    --tagline-ink: #0e6aa8;
    --brand-blue: #3bbfee;
    --white: #ffffff;
    --soft-white: #d9e4f0;
  }
  html, body {
    margin: 0;
    padding: 0;
    width: 1200px;
    height: 801px;
    overflow: hidden;
    background: var(--stage);
  }
  .sheet {
    position: relative;
    width: 1200px;
    height: 801px;
  }
  .card {
    position: absolute;
    top: 274px;
    width: 443px;
    height: 263px;
    overflow: hidden;
  }
  .card--front {
    left: 153px;
    background: linear-gradient(35deg, var(--navy) 0%, var(--navy) 45%, var(--navy-lift) 100%);
    color: var(--white);
    font-family: "Roboto", Arial, sans-serif;
  }
  .holder {
    position: absolute;
    left: 25px;
    top: 62px;
  }
  .holder__name {
    margin: 0;
    font-family: "Lato", Arial, sans-serif;
    font-weight: 700;
    font-size: 17px;
    line-height: 19px;
    letter-spacing: -0.2px;
  }
  .holder__role {
    margin: 0;
    font-size: 13px;
    line-height: 15px;
  }
  .contact {
    position: absolute;
    left: 25px;
    top: 104px;
    margin: 0;
    padding: 0;
    list-style: none;
    font-size: 13px;
    line-height: 15.7px;
  }
  .contact li {
    display: flex;
    align-items: center;
    gap: 4px;
  }
  .contact svg {
    width: 11px;
    height: 11px;
    flex: none;
  }
  .address {
    position: absolute;
    left: 25px;
    top: 164px;
    margin: 0;
    font-style: normal;
    font-size: 13px;
    line-height: 15.7px;
  }
  .services {
    position: absolute;
    left: 262px;
    top: 64px;
    width: 160px;
    padding-left: 14px;
    border-left: 2px solid var(--brand-blue);
  }
  .services__title {
    margin: 0 0 6px;
    font-family: "Lato", Arial, sans-serif;
    font-weight: 700;
    font-size: 12px;
    line-height: 14px;
    letter-spacing: 1px;
    color: var(--brand-blue);
  }
  .services__list {
    margin: 0;
    padding: 0;
    list-style: none;
    font-size: 11.5px;
    line-height: 20px;
    color: var(--soft-white);
  }
  .services__list li {
    display: flex;
    align-items: center;
    gap: 6px;
  }
  .services__list li::before {
    content: "";
    width: 5px;
    height: 5px;
    border-radius: 50%;
    background: var(--brand-blue);
    flex: none;
  }
  .card--back {
    left: 625px;
    background: var(--card-dark);
  }
  .brand {
    position: absolute;
    left: 0;
    right: 0;
    top: 86px;
    display: flex;
    justify-content: center;
    align-items: center;
    gap: 10px;
  }
  .brand__dot {
    width: 30px;
    height: 30px;
    border-radius: 50%;
    background: var(--brand-blue);
  }
  .brand__name {
    font-family: "Lato", Arial, sans-serif;
    font-weight: 700;
    font-size: 50px;
    line-height: 1;
    color: var(--brand-blue);
    letter-spacing: -1.5px;
  }
  .tagline {
    position: absolute;
    left: 0;
    width: 443px;
    top: 192px;
    height: 22px;
    margin: 0;
    background: var(--blue-pale);
    color: var(--tagline-ink);
    font-family: "Roboto", Arial, sans-serif;
    font-weight: 700;
    font-size: 12.6px;
    line-height: 22px;
    text-align: center;
    letter-spacing: 0.1px;
  }
</style>
</head>
<body>
<main class="sheet">
  <section class="card card--front" aria-label="Business card front">
    <div class="holder">
      <h1 class="holder__name">DANIEL HARPER</h1>
      <p class="holder__role">Managing Director</p>
    </div>
    <ul class="contact">
      <li>
        <svg viewBox="0 0 24 24" aria-hidden="true"><path fill="#fff" d="M6.6 10.8a15.1 15.1 0 0 0 6.6 6.6l2.2-2.2c.3-.3.7-.4 1-.2 1.1.4 2.3.6 3.6.6.6 0 1 .4 1 1V20c0 .6-.4 1-1 1A17 17 0 0 1 3 4c0-.6.4-1 1-1h3.5c.6 0 1 .4 1 1 0 1.3.2 2.5.6 3.6.1.3 0 .7-.2 1z"/></svg>
        <span>84 0900 555 214</span>
      </li>
      <li>
        <svg viewBox="0 0 24 24" aria-hidden="true"><path fill="#fff" d="M2 5h20v14H2z"/><path fill="none" stroke="#192841" stroke-width="1.6" d="M2 5l10 8 10-8"/></svg>
        <span>info@brovexa.com</span>
      </li>
      <li>
        <svg viewBox="0 0 24 24" aria-hidden="true"><g fill="none" stroke="#fff" stroke-width="2"><circle cx="12" cy="12" r="10"/><ellipse cx="12" cy="12" rx="4" ry="10"/><path d="M2 12h20M4 7h16M4 17h16"/></g></svg>
        <span>www.brovexa.com</span>
      </li>
    </ul>
    <address class="address">42 Tran Quang Lane<br>Dong Da, Ha Noi</address>

    <div class="services">
      <h2 class="services__title">SERVICES</h2>
      <ul class="services__list">
        <li>Whole Home Water Filters</li>
        <li>Salt Free Water Softeners</li>
        <li>Clarimont KT7</li>
        <li>UV Sterilizers</li>
      </ul>
    </div>
  </section>

  <section class="card card--back" aria-label="Business card back">
    <div class="brand">
      <span class="brand__dot" aria-hidden="true"></span>
      <span class="brand__name">BroVexa</span>
    </div>
    <p class="tagline">SPRING QUALITY ALKALINE WATER AT EVERY TAP</p>
  </section>
</main>
</body>
</html>
```